Business Card Design

my company buys cars,boats and caravans off the public, and also assists the public in helping them sell there item(brokering),i have an idea of a logo which is.....T$A....THE S BEING A LARGE DOLLAR SIGN,centred. And underneath my business name....TRADER-HOLDER-AGENT,i like black backgrounds, CLEAN SHARP AND TO THE POINT!!

Industry/Entity Type

Business

Contact Information for Business Card

$wap NOWLY.........buyer,seller,broker......cars,boats,caravans...........0427591846.......-swapnowly@traderholderagent.com.au, lmct-58417

Requirements
Must have
• MOBILE NUMBER-0427591846
EMAIL-swapnowly@traderholderagent.com.au
business name-TRADER-HOLDER-AGENT
lmct-58417
what we deal in-Cars,Caravans,Boats
cash,bank chq, finance paid out
Nice to have
• clever logo created by you guys

```html
<!DOCTYPE html>
<html lang="en">
<head>
<meta charset="UTF-8">
<title>Trader-Holder-Agent Business Card</title>
<link rel="stylesheet" href="https://fonts.googleapis.com/css2?family=Poiret+One&family=Questrial&display=swap">
<style>
  :root {
    --backdrop: #d6d6d6;
    --card: #fbfbfb;
    --ink: #141414;
    --rule: #1c1c1c;
  }
  * { margin: 0; padding: 0; box-sizing: border-box; }
  html, body {
    width: 1200px;
    height: 765px;
    overflow: hidden;
    background: var(--backdrop);
  }
  .canvas {
    position: relative;
    width: 1200px;
    height: 765px;
    display: flex;
    align-items: center;
    justify-content: center;
  }
  .business-card {
    position: relative;
    width: 1120px;
    height: 620px;
    background: var(--card);
    color: var(--ink);
    text-align: center;
    font-family: "Questrial", "Century Gothic", sans-serif;
  }
  .business-name {
    position: absolute;
    top: 78px;
    left: 0;
    right: 0;
    font-family: "Poiret One", "Century Gothic", sans-serif;
    font-weight: 400;
    font-size: 58px;
    letter-spacing: 1px;
  }
  .name-rule {
    position: absolute;
    top: 172px;
    left: 290px;
    width: 540px;
    height: 2px;
    background: var(--rule);
  }
  .contact-list {
    position: absolute;
    top: 262px;
    left: 0;
    right: 0;
    list-style: none;
    font-size: 29px;
    line-height: 51px;
  }
  .offer-list {
    position: absolute;
    top: 456px;
    left: 0;
    right: 0;
    list-style: none;
    font-size: 28px;
    line-height: 52px;
  }
</style>
</head>
<body>
  <main class="canvas">
    <section class="business-card" aria-label="Trader-Holder-Agent business card">
      <h1 class="business-name">Trader-Holder-Agent</h1>
      <div class="name-rule"></div>
      <ul class="contact-list">
        <li class="contact-mobile">Mobile No:-&nbsp; 0427591846</li>
        <li class="contact-email">Email:- swapnowly@traderholderagent.com.au</li>
        <li class="contact-licence">lMCT:- 58417</li>
      </ul>
      <ul class="offer-list">
        <li class="offer-stock">deal in-Cars,Caravans,Boats</li>
        <li class="offer-payment">cash,bank chq, finance paid out</li>
      </ul>
    </section>
  </main>
</body>
</html>
```